Rising Side by Side A Handbook to Guide Managers and Crews Toward Greater Levels of Output

We need a book cover design for a book titled: Rising Side by Side:
A Handbook to Guide Managers and Crews Toward Greater Levels of Output
The book is intended to enhance the author's personal brand and promote the author's consulting services. The book also teaches: How To Help Leaders and Teams Reach New Heights of Performance. I would like to use the colors from the www.brindlemoorworks.example website (blue and orange). The design should communicate credibility and expertise in the topic of the book.

Target Market(s)

Municipal and Industrial and Energy Industry Team Leaders and Teams

Industry/Entity Type

water and waste water, energy, power generation, petrochmical

Requirements
Must have
• Look like a Dalbrook Ledger best seller. Look professional and appealling
Nice to have
• Sell at the airport. Executives keep in their office.
Should not have
• Do not plagiarize.

```html
<!DOCTYPE html>
<html lang="en">
<head>
<meta charset="utf-8">
<title>Rising Side by Side — Book Cover</title>
<link rel="stylesheet" href="https://fonts.googleapis.com/css2?family=Cinzel:wght@400;500&display=swap">
<style>
  :root {
    --page-bg: #e6e6e6;
    --ink: #1b3138;
    --author-ink: #f3f5f5;
    --award-orange: #e08a2c;
    --award-gold: #d9a542;
  }
  html, body {
    margin: 0;
    width: 1200px;
    height: 800px;
    overflow: hidden;
    background: var(--page-bg);
  }
  .canvas {
    position: relative;
    width: 1200px;
    height: 800px;
  }
  .cover {
    position: absolute;
    left: 408px;
    top: 94px;
    width: 398px;
    height: 608px;
    overflow: hidden;
    font-family: "Cinzel", "Times New Roman", serif;
    color: var(--ink);
  }
  .cover-art {
    position: absolute;
    inset: 0;
    width: 398px;
    height: 608px;
  }
  .title {
    position: absolute;
    inset: 0 0 auto 0;
    margin: 0;
    text-align: center;
    font-weight: 400;
    line-height: 1;
  }
  .title-word {
    display: block;
    position: absolute;
    left: 0;
    width: 100%;
  }
  .title-main { font-size: 80px; letter-spacing: 1px; }
  .title-joiner { font-size: 28px; letter-spacing: 1px; }
  .title-first { top: 44px; }
  .title-middle { top: 140px; }
  .title-last { top: 182px; }
  .award-area {
    position: absolute;
    left: 158px;
    top: 309px;
    width: 84px;
    height: 92px;
    border-radius: 40px 40px 8px 8px;
    background: linear-gradient(180deg, var(--award-gold), var(--award-orange));
  }
  .subtitle {
    position: absolute;
    left: 35px;
    top: 426px;
    width: 326px;
    margin: 0;
    text-align: center;
    font-size: 16px;
    line-height: 24px;
    font-weight: 400;
    letter-spacing: 0.3px;
  }
  .author {
    position: absolute;
    left: 0;
    top: 564px;
    width: 100%;
    margin: 0;
    text-align: center;
    font-size: 20px;
    letter-spacing: 1px;
    color: var(--author-ink);
    font-weight: 400;
  }
</style>
</head>
<body>
<div class="canvas">
  <div class="cover">
    <svg class="cover-art" viewBox="0 0 398 608" xmlns="http://www.w3.org/2000/svg" aria-hidden="true">
      <defs>
        <linearGradient id="sky" x1="0" y1="0" x2="0" y2="1">
          <stop offset="0" stop-color="#e8ebe9"/>
          <stop offset="0.5" stop-color="#f1f2f1"/>
          <stop offset="0.62" stop-color="#f3f4f4"/>
          <stop offset="0.66" stop-color="#dfe6e8"/>
          <stop offset="1" stop-color="#cbd7db"/>
        </linearGradient>
        <linearGradient id="wall" x1="0" y1="0" x2="0" y2="1">
          <stop offset="0" stop-color="#c6d3d7"/>
          <stop offset="0.5" stop-color="#8eaab3"/>
          <stop offset="1" stop-color="#3f6c7a"/>
        </linearGradient>
        <linearGradient id="panel" x1="0" y1="0" x2="0" y2="1">
          <stop offset="0" stop-color="#bccdd2"/>
          <stop offset="1" stop-color="#a9bdc4"/>
        </linearGradient>
        <linearGradient id="base" x1="0" y1="0" x2="0" y2="1">
          <stop offset="0" stop-color="#2c5b69"/>
          <stop offset="1" stop-color="#1a4150"/>
        </linearGradient>
      </defs>
      <rect class="backdrop" x="0" y="0" width="398" height="608" fill="url(#sky)"/>
      <rect class="wall-left" x="0" y="330" width="35" height="278" fill="url(#wall)"/>
      <rect class="wall-right" x="361" y="330" width="37" height="278" fill="url(#wall)"/>
      <rect class="wall-left-face" x="28" y="336" width="7" height="65" fill="#d7e0e3"/>
      <rect class="wall-right-face" x="361" y="336" width="7" height="65" fill="#d7e0e3"/>
      <rect class="ledge" x="35" y="399" width="326" height="4" fill="#dbe4e6"/>
      <rect class="front-panel" x="35" y="403" width="326" height="137" fill="url(#panel)"/>
      <rect class="step-left" x="0" y="470" width="35" height="138" fill="#37636f"/>
      <rect class="step-right" x="361" y="470" width="37" height="138" fill="#37636f"/>
      <rect class="base-band" x="0" y="540" width="398" height="68" fill="url(#base)"/>
      <rect class="spine-highlight" x="8" y="0" width="6" height="608" fill="#ffffff" opacity="0.35"/>
    </svg>

    <h1 class="title">
      <span class="title-word title-main title-first">RISING</span>
      <span class="title-word title-joiner title-middle">SIDE BY</span>
      <span class="title-word title-main title-last">SIDE</span>
    </h1>

    <div class="award-area" role="img" aria-label="Image area: a golden trophy cup standing on the ledge"></div>

    <h2 class="subtitle">A HANDBOOK TO GUIDE<br>MANAGERS AND CREWS TOWARD<br>GREATER LEVELS<br>OF OUTPUT</h2>

    <p class="author">MAREN HOLLOWAY VANCE</p>
  </div>
</div>
</body>
</html>
```